Brennick Holdings Business Cards

These are professional business cards that are for my family office.
Put fake emails and phone numbers as of now until I finalize those components. This family office controls my families investments, assets, and future. The cards should be professional.
..
.
.
.
I just uploaded another variation of a logo I would like to see as a business card to I am inbeteen which logo to use

Target Market(s)

business

Industry/Entity Type

business

Contact Information for Business Card

Professional, wealth related, finance related.

Requirements
Must have
• Logo

```html
<!DOCTYPE html>
<html lang="en">
<head>
<meta charset="utf-8">
<title>Brennick Holdings Business Cards</title>
<link rel="stylesheet" href="https://fonts.googleapis.com/css2?family=Cinzel:wght@400;700&display=swap">
<style>
  :root {
    --navy: #1a1f2c;
    --paper: #e9eaec;
    --backdrop: #f3f4f6;
    --white: #ffffff;
    --grey: #a3a3a3;
    --ink: #1a1f2c;
  }
  * { margin: 0; padding: 0; box-sizing: border-box; }
  html, body { width: 1200px; height: 1200px; overflow: hidden; }
  body {
    position: relative;
    background: var(--backdrop);
    font-family: "Cinzel", "Times New Roman", serif;
  }
  .card {
    position: absolute;
    left: 169px;
    width: 862px;
    height: 496px;
    overflow: hidden;
  }
  .card-front { top: 59px; background: var(--navy); color: var(--white); }
  .card-back { top: 619px; background: var(--paper); color: var(--ink); }

  .front-mark {
    position: absolute;
    left: 396px; top: 148px;
    width: 126px; height: 126px;
    border: 2.5px solid var(--white);
    border-radius: 50%;
  }
  .front-name {
    position: absolute;
    left: 0; right: 0; top: 306px;
    text-align: center;
    font-size: 34px;
    font-weight: 400;
    letter-spacing: 1px;
  }
  .front-web {
    position: absolute;
    left: 0; right: 0; top: 430px;
    text-align: center;
    font-size: 17px;
    letter-spacing: 4px;
  }

  .person-name {
    position: absolute;
    left: 79px; top: 92px;
    font-size: 44px;
    font-weight: 700;
    letter-spacing: 0.5px;
  }
  .person-role {
    position: absolute;
    left: 79px; width: 350px; top: 153px;
    text-align: right;
    font-size: 23px;
    color: var(--grey);
    letter-spacing: 1px;
  }

  .contact-list { list-style: none; }
  .contact-icon {
    position: absolute;
    left: 66px;
    width: 46px; height: 46px;
    border-radius: 50%;
    background: var(--grey);
    display: flex; align-items: center; justify-content: center;
  }
  .contact-text {
    position: absolute;
    left: 131px;
    font-size: 26px;
    line-height: 36px;
    white-space: nowrap;
  }
  .contact-phone .contact-icon { top: 252px; }
  .contact-phone .contact-text { top: 257px; }
  .contact-address .contact-icon { top: 319px; }
  .contact-address .contact-text { top: 308px; }
  .contact-email .contact-icon { top: 384px; }
  .contact-email .contact-text { top: 389px; }

  .brand-tab {
    position: absolute;
    left: 536px; top: 0;
    width: 269px; height: 321px;
    background: var(--navy);
    border-radius: 0 0 134px 134px;
  }
  .tab-mark {
    position: absolute;
    left: 52px; top: 108px;
    width: 166px; height: 166px;
    border: 3px solid var(--white);
    border-radius: 50%;
  }
</style>
</head>
<body>
  <section class="card card-front">
    <div class="front-mark"></div>
    <h1 class="front-name">Brennick Holdings</h1>
    <p class="front-web">WWW.BRENNICKHOLDINGS.COM</p>
  </section>

  <section class="card card-back">
    <h2 class="person-name">Adrian Brennick</h2>
    <p class="person-role">Owner</p>
    <ul class="contact-list">
      <li class="contact-phone">
        <span class="contact-icon">
          <svg width="24" height="24" viewBox="0 0 24 24" fill="none" stroke="#fff" stroke-width="1.8" stroke-linejoin="round"><path d="M6.5 3.5l3 3.5-2 2.2a11 11 0 0 0 7.3 7.3l2.2-2 3.5 3-2 2.5C12 20 4 12 4 5.5z"/></svg>
        </span>
        <span class="contact-text">+1 555 014-2273</span>
      </li>
      <li class="contact-address">
        <span class="contact-icon">
          <svg width="24" height="24" viewBox="0 0 24 24" fill="none" stroke="#fff" stroke-width="2"><path d="M12 21s-6-6.2-6-11a6 6 0 0 1 12 0c0 4.8-6 11-6 11z"/><circle cx="12" cy="10" r="2.2"/></svg>
        </span>
        <span class="contact-text">18th Floor. 210 Harlow Ave,<br>Ashford, CT 06278, USA.</span>
      </li>
      <li class="contact-email">
        <span class="contact-icon">
          <svg width="24" height="24" viewBox="0 0 24 24" fill="none" stroke="#fff" stroke-width="1.8" stroke-linejoin="round"><rect x="3.5" y="6" width="17" height="12"/><path d="M3.5 6l8.5 7 8.5-7"/></svg>
        </span>
        <span class="contact-text">Office@brennick.com</span>
      </li>
    </ul>
    <div class="brand-tab">
      <div class="tab-mark"></div>
    </div>
  </section>
</body>
</html>
```